Healthcare IT firm needs classy and unique business care design

We need a business card design that incorporates our new logo design (attached) Prefer a purple based designed. I would really love to see something utilizing the "3D" version of the logo (purple on the reflective wall). I want something a little more than my logo printed along with a person's detailed contact information.
Contact Information for Business Card
Want something polished, professional, and a little unique in the design.
Colors
6b449b
Requirements
Must have
- Please use similar font as the logo design
Nice to have
- Would like to see the 3d version of my logo incorporated into the design.

```html
<!DOCTYPE html>
<html lang="en">
<head>
<meta charset="utf-8">
<title>Corvana Health Systems — Business Card</title>
<link href="https://fonts.googleapis.com/css2?family=Roboto:wght@400;500;700&display=swap" rel="stylesheet">
<style>
  :root {
    --brand-purple: #6b449b;
    --card-white: #ffffff;
    --ink: #4a4a4a;
    --backdrop: #2c2c2e;
    --foil: #dcdce2;
  }
  * { margin: 0; padding: 0; box-sizing: border-box; }
  html, body { width: 1200px; height: 960px; overflow: hidden; }
  body {
    background: var(--backdrop);
    font-family: 'Roboto', sans-serif;
    position: relative;
  }
  .card {
    position: absolute;
    width: 600px;
    height: 342px;
    box-shadow: 0 3px 8px rgba(0,0,0,0.45);
  }
  .card-front { left: 322px; top: 110px; background: var(--card-white); }
  .card-back  { left: 320px; top: 493px; background: var(--brand-purple); }

  .wordmark {
    position: absolute;
    left: 38px;
    top: 48px;
    display: flex;
    align-items: center;
    gap: 10px;
    font-size: 25px;
    font-weight: 700;
    color: var(--brand-purple);
    white-space: nowrap;
  }
  .wordmark-square {
    width: 22px; height: 22px;
    background: var(--brand-purple);
  }

  .address {
    position: absolute;
    left: 37px;
    top: 171px;
    font-size: 14px;
    line-height: 18px;
    color: var(--ink);
  }
  .contact-list {
    position: absolute;
    left: 37px;
    top: 217px;
    list-style: none;
    font-size: 14px;
    color: var(--ink);
  }
  .contact-list li {
    display: flex;
    align-items: center;
    height: 19px;
  }
  .contact-icon {
    width: 13px; height: 13px;
    margin-right: 10px;
    fill: var(--brand-purple);
  }

  .name-band {
    position: absolute;
    left: 407px;
    right: 0;
    top: 212px;
    height: 61px;
    background: var(--brand-purple);
    color: var(--card-white);
    text-align: right;
    padding: 6px 32px 0 0;
  }
  .person-name { font-size: 23px; font-weight: 500; line-height: 28px; }
  .person-title { font-size: 16px; font-weight: 500; line-height: 20px; }

  .back-wordmark {
    position: absolute;
    left: 0; right: 0;
    top: 148px;
    text-align: center;
    font-size: 34px;
    font-weight: 700;
    color: var(--foil);
    white-space: nowrap;
  }
</style>
</head>
<body>
  <section class="card card-front">
    <div class="wordmark"><span class="wordmark-square"></span>Corvana Health Systems</div>

    <address class="address" style="font-style:normal">
      4120 Birchwood Court<br>
      Fairbanks, Alaska 99701
    </address>

    <ul class="contact-list">
      <li>
        <svg class="contact-icon" viewBox="0 0 24 24" aria-hidden="true"><path d="M6.6 10.8a15.1 15.1 0 0 0 6.6 6.6l2.2-2.2a1 1 0 0 1 1-.25 11.4 11.4 0 0 0 3.6.57 1 1 0 0 1 1 1V20a1 1 0 0 1-1 1A17 17 0 0 1 3 4a1 1 0 0 1 1-1h3.5a1 1 0 0 1 1 1c0 1.25.2 2.45.57 3.57a1 1 0 0 1-.25 1z"/></svg>
        555 210 4471
      </li>
      <li>
        <svg class="contact-icon" viewBox="0 0 24 24" aria-hidden="true"><path d="M7 1h10a2 2 0 0 1 2 2v18a2 2 0 0 1-2 2H7a2 2 0 0 1-2-2V3a2 2 0 0 1 2-2zm0 3v14h10V4zm5 15.2a1.2 1.2 0 1 0 0 2.4 1.2 1.2 0 0 0 0-2.4z"/></svg>
        555 318 6620
      </li>
      <li>
        <svg class="contact-icon" viewBox="0 0 24 24" aria-hidden="true"><path d="M6 2h10v6H6zM3 9h18a1 1 0 0 1 1 1v8h-4v4H6v-4H2v-8a1 1 0 0 1 1-1zm5 7v4h8v-4z"/></svg>
        555 742 0193
      </li>
      <li>
        <svg class="contact-icon" viewBox="0 0 24 24" aria-hidden="true"><path d="M2 5h20v14H2zm2 2v.5l8 5 8-5V7zm0 2.9V17h16V9.9l-8 5z"/></svg>
        hello@corvanahealth.com
      </li>
      <li>
        <svg class="contact-icon" viewBox="0 0 24 24" aria-hidden="true"><path d="M12 2a10 10 0 1 0 0 20 10 10 0 0 0 0-20zm-1 17.9A8 8 0 0 1 4.2 10.3L9 15v1a2 2 0 0 0 2 2zm6.9-2.5A2 2 0 0 0 16 16h-1v-3a1 1 0 0 0-1-1H8v-2h2a1 1 0 0 0 1-1V7h2a2 2 0 0 0 2-2v-.4a8 8 0 0 1 2.9 12.8z"/></svg>
        www.corvanahealth.com
      </li>
    </ul>

    <div class="name-band">
      <div class="person-name">Daniel Reyes</div>
      <div class="person-title">CEO/Founder</div>
    </div>
  </section>

  <section class="card card-back">
    <div class="back-wordmark">Corvana Health Systems</div>
  </section>
</body>
</html>
```